Business Card Design

I am nail technician working from home in Mount Helena, Perth and I require new business cards. I only work with Gel medium for nail extensions using tips or I can also do sculpture nails. I specialise in hand painted nail art using water based acrylic paint and nail polish. As the name suggest I love all things "Velvet" so I would love something that reflects this while also being professional. I'm also on Trendlo and would the Trendlo logo.

Contact Information for Business Card

Velvet Comet nail designs,Rosalind ,0417859273, VelvetCometnaildesigns@quorvia.com, nail technician specialising in hand painted nail art, only using a Gel medium

```html
<!DOCTYPE html>
<html lang="en">
<head>
<meta charset="utf-8">
<title>Velvet Comet Nail Designs – Business Cards</title>
<link rel="stylesheet" href="https://fonts.googleapis.com/css2?family=Niconne&family=Open+Sans:ital,wght@0,400;0,600;1,400&display=swap">
<style>
  :root {
    --page-bg: #eeeae6;
    --card-white: #ffffff;
    --swoosh-grey: #cfcfd1;
    --brand-red: #d8101f;
    --brand-red-light: #e8192a;
    --brand-red-dark: #a40a15;
    --band-red: #8c0911;
    --ink-grey: #5a5a5a;
    --text-white: #ffffff;
  }
  html, body {
    margin: 0;
    padding: 0;
    width: 1200px;
    height: 1024px;
    overflow: hidden;
    background: var(--page-bg);
  }
  .canvas {
    position: relative;
    width: 1200px;
    height: 1024px;
  }
  .card {
    position: absolute;
    left: 190px;
    width: 820px;
    height: 468px;
    overflow: hidden;
    box-shadow: 0 6px 20px rgba(0,0,0,0.18);
  }
  .card--front { top: 30px; background: var(--card-white); }
  .card--back {
    top: 526px;
    background: radial-gradient(ellipse at 55% 35%, var(--brand-red-light) 0%, var(--brand-red) 50%, var(--brand-red-dark) 100%);
  }
  .card__shapes { position: absolute; inset: 0; }

  .brand {
    position: absolute;
    margin: 0;
    line-height: 1.1;
    font-family: "Open Sans", sans-serif;
    font-weight: 600;
    font-style: normal;
    white-space: nowrap;
  }
  .card--front .brand {
    left: 52px;
    top: 170px;
    font-size: 34px;
    color: var(--brand-red);
  }

  .holder {
    position: absolute;
    right: 40px;
    top: 38px;
    margin: 0;
    font-family: "Niconne", cursive;
    font-size: 58px;
    font-weight: 400;
    color: var(--ink-grey);
  }

  .contact {
    position: absolute;
    left: 56px;
    bottom: 40px;
    margin: 0;
    padding: 0;
    list-style: none;
    font-family: "Open Sans", sans-serif;
    font-size: 19px;
    color: var(--text-white);
  }
  .contact__item { display: flex; align-items: center; gap: 16px; height: 40px; }
  .contact__icon { width: 20px; height: 20px; flex: none; }

  .card--back .brand {
    left: 0; right: 0; top: 150px;
    text-align: center;
    font-size: 56px;
    color: var(--text-white);
  }

  .tagline-band {
    position: absolute;
    left: 0; right: 0; bottom: 0;
    height: 118px;
    background: var(--band-red);
    display: flex;
    align-items: center;
    justify-content: center;
  }
  .tagline {
    margin: 0;
    font-family: "Open Sans", sans-serif;
    font-style: italic;
    font-size: 21px;
    line-height: 1.45;
    color: var(--text-white);
    text-align: center;
  }
</style>
</head>
<body>
<main class="canvas">

  <section class="card card--front" aria-label="Business card front">
    <svg class="card__shapes" viewBox="0 0 820 468" preserveAspectRatio="none" aria-hidden="true">
      <defs>
        <linearGradient id="front-red" x1="0" y1="0" x2="0" y2="1">
          <stop offset="0" stop-color="#e8192a"/>
          <stop offset="1" stop-color="#b60c18"/>
        </linearGradient>
      </defs>
      <path d="M300 468 C420 330 520 200 600 120 C660 60 740 30 820 20 L820 468 Z" fill="var(--swoosh-grey)"/>
      <path d="M0 330 C220 330 400 270 520 170 C600 105 700 100 820 120 L820 468 L0 468 Z" fill="#ffffff"/>
      <path d="M0 340 C230 340 410 285 530 190 C610 128 710 125 820 145 L820 468 L0 468 Z" fill="url(#front-red)"/>
    </svg>

    <h1 class="brand">Velvet Comet Nail Designs</h1>

    <p class="holder">Rosalind</p>

    <ul class="contact">
      <li class="contact__item">
        <svg class="contact__icon" viewBox="0 0 24 24" aria-hidden="true">
          <path d="M6.6 2.5c.6-.3 1.3-.1 1.6.5l1.8 3.4c.3.6.1 1.2-.4 1.6L8.2 9c.9 2.6 3.9 5.7 6.6 6.7l1.1-1.4c.4-.5 1.1-.6 1.6-.3l3.300 1.9c.6.3.8 1 .5 1.6l-1.2 2.3c-.5.9-1.5 1.4-2.5 1.2C10.5 19.6 4.3 13.4 3 6.3c-.2-1 .3-2 1.2-2.5z" fill="#ffffff"/>
        </svg>
        <span>0417859273</span>
      </li>
      <li class="contact__item">
        <svg class="contact__icon" viewBox="0 0 24 24" aria-hidden="true">
          <rect x="2" y="5" width="20" height="14" rx="2" fill="#ffffff"/>
          <path d="M3 6.5 L12 13 L21 6.5" fill="none" stroke="#d8101f" stroke-width="1.8"/>
        </svg>
        <span>VelvetCometnaildesigns@quorvia.com</span>
      </li>
    </ul>
  </section>

  <section class="card card--back" aria-label="Business card back">
    <h2 class="brand">Velvet Comet Nail Designs</h2>
    <div class="tagline-band">
      <p class="tagline">Nail technician specialising in hand painted nail art,<br>only using a Gel medium</p>
    </div>
  </section>

</main>
</body>
</html>
```